High End Notary Service Business Card Design

Want a professional and elegant/luxurious business card that is clean and simple in the design. A notary is a trusted professional that helps people sign very important documents. The card should be in alignment with this service provided.

Most of the time, service will be for the purchase of a home or refinance of a mortgage

There is NO LOGO. This is aesthetic. A look and feel. Conveying professionalism and concierge level of service.

Target Market(s)

Other business professionals, Lawyers, Escrow Officers, Loan Officers

Industry/Entity Type

Legal

Contact Information for Business Card

This will be a one-sided business card

Colors
35a7d7
3176b5
85cae6
d3a5cc
b868aa
ffffff
0356a4

Requirements
Must have
• Lorena T. Mirabel-Hodgkins
Notary Public

642-871-3094
MirabelSigningDesk@Wexmail.com
Nice to have
• Headshot photo below. Convey the aspect of signing documents. No black cards. Preference is shades of blue: light blue, navy, aqua, gold, white, or lavendar, etc.
Should not have
• No scales or legal scales.

```html
<!DOCTYPE html>
<html lang="en">
<head>
<meta charset="utf-8">
<title>Lorena T. Mirabel-Hodgkins – Notary Public</title>
<link rel="stylesheet" href="https://fonts.googleapis.com/css2?family=Arimo:wght@400;700&display=swap">
<style>
  :root {
    --backdrop: #2b2b2b;
    --card: #ffffff;
    --name-blue: #2f73bd;
    --text-grey: #6f6f6f;
    --rule: #d6d6d6;
    --photo-dark: #7c7c7c;
    --photo-mid: #b9b9b9;
    --photo-light: #e6e6e6;
  }
  html, body {
    margin: 0;
    width: 1200px;
    height: 900px;
    overflow: hidden;
    background: var(--backdrop);
  }
  .business-card {
    position: absolute;
    left: 100px;
    top: 160px;
    width: 1000px;
    height: 580px;
    background: var(--card);
    overflow: hidden;
    font-family: "Arimo", Helvetica, Arial, sans-serif;
  }
  .headshot {
    position: absolute;
    left: 0;
    top: 0;
    width: 560px;
    height: 580px;
    background:
      radial-gradient(ellipse 48% 55% at 42% 60%, var(--photo-dark) 0%, var(--photo-mid) 50%, rgba(230,230,230,0) 100%),
      linear-gradient(90deg, var(--photo-light) 0%, var(--photo-light) 55%, rgba(255,255,255,0) 100%);
  }
  .contact-block {
    position: absolute;
    left: 455px;
    top: 232px;
  }
  .holder-name {
    margin: 0;
    font-weight: 700;
    font-size: 28px;
    letter-spacing: 0.2px;
    text-transform: uppercase;
    color: var(--name-blue);
  }
  .holder-title {
    margin: 4px 0 0;
    font-size: 27px;
    color: var(--text-grey);
  }
  .divider {
    width: 200px;
    height: 1px;
    background: var(--rule);
    margin: 20px 0 22px;
  }
  .contact-line {
    margin: 0 0 4px;
    font-size: 26px;
    color: var(--text-grey);
  }
</style>
</head>
<body>
  <main class="business-card">
    <div class="headshot" role="img" aria-label="Black and white headshot of the notary, smiling, shoulder-length hair"></div>
    <div class="contact-block">
      <h1 class="holder-name">Lorena T. Mirabel-Hodgkins</h1>
      <p class="holder-title">Notary Public</p>
      <div class="divider"></div>
      <p class="contact-line">642-871-3094</p>
      <p class="contact-line">MirabelSigningDesk@Wexmail.com</p>
    </div>
  </main>
</body>
</html>
```